ALL TEXT Social Media Graphics

We are looking for a series of social media graphics for Instagram (new size: 4:5 (1080 x 1350 pixels) ratio that are ALL TEXT. We want the following quotes below on each graphic; one quote per graphic. AND, In very small letters at the bottom of each graphic, add @PaulaWrenLive
The look and feel of these graphics should be complimentary to the color palette attached below; but keep them simple. But the design is up to you; at the end of this document, I provided various samples of all text graphics that I like as examples.
The Quotes are in the attached WORD document
women trying to lose weight

```html
<!DOCTYPE html>
<html lang="en">
<head>
<meta charset="utf-8">
<title>Summer Slimdown – All Text Social Graphics</title>
<link rel="stylesheet" href="https://fonts.googleapis.com/css2?family=Anton&family=Source+Sans+3:wght@400;600&display=swap">
<style>
  :root {
    --backdrop: #d6d6d6;
    --card: #ffffff;
    --berry: #d4306c;
    --blush: #f06595;
    --white: #ffffff;
  }
  html, body {
    margin: 0;
    padding: 0;
    width: 1200px;
    height: 3280px;
    overflow: hidden;
    background: var(--backdrop);
  }
  .board {
    position: relative;
    width: 1200px;
    height: 3280px;
  }
  .post {
    position: absolute;
    width: 460px;
    height: 575px;
    background: var(--card);
    overflow: hidden;
  }
  .col-left { left: 112px; }
  .col-right { left: 628px; }
  .row-1 { top: 93px; }
  .row-2 { top: 724px; }
  .row-3 { top: 1353px; }
  .row-4 { top: 1984px; }
  .row-5 { top: 2614px; }

  .line {
    position: absolute;
    margin: 0;
    white-space: nowrap;
    font-family: "Anton", "Impact", sans-serif;
    font-weight: 400;
    line-height: 1;
    color: var(--berry);
    text-transform: uppercase;
  }
  .center { left: 0; right: 0; text-align: center; }
  .berry { color: var(--berry); }
  .blush { color: var(--blush); }

  .body-copy {
    position: absolute;
    margin: 0;
    white-space: nowrap;
    font-family: "Source Sans 3", "Helvetica Neue", Arial, sans-serif;
    font-weight: 400;
    color: var(--berry);
    line-height: 1.2;
  }
  .handle {
    position: absolute;
    margin: 0;
    font-family: "Source Sans 3", "Helvetica Neue", Arial, sans-serif;
    font-size: 17px;
    color: var(--berry);
    line-height: 1;
  }

  .band {
    position: absolute;
    left: 0;
    width: 460px;
    display: flex;
    align-items: center;
    box-sizing: border-box;
    font-family: "Anton", "Impact", sans-serif;
    color: var(--white);
    white-space: nowrap;
    text-transform: uppercase;
    line-height: 1;
  }
  .band-berry { background: var(--berry); }
  .band-blush { background: var(--blush); }
  .band-center { justify-content: center; }

  .framed-figure {
    position: absolute;
    box-sizing: border-box;
    border: 4px solid var(--berry);
    display: flex;
    align-items: center;
    justify-content: center;
    font-family: "Anton", "Impact", sans-serif;
    color: var(--berry);
    line-height: 1;
  }

  .checklist {
    position: absolute;
    margin: 0;
    padding: 0;
    list-style: none;
  }
  .checklist li {
    display: flex;
    align-items: center;
    height: 55px;
    font-family: "Anton", "Impact", sans-serif;
    font-size: 42px;
    color: var(--berry);
    white-space: nowrap;
    line-height: 1;
  }
  .checklist svg {
    width: 46px;
    height: 46px;
    margin-right: 16px;
    flex: none;
  }
</style>
</head>
<body>
<main class="board">

  <!-- Post 1 -->
  <section class="post col-left row-1">
    <h2 class="line center" style="top:30px;font-size:62px;">You don’t need</h2>
    <h2 class="line center" style="top:108px;font-size:68px;">another diet</h2>
    <p class="line center" style="top:212px;font-size:26px;">You need a system that works !</p>
    <div class="band band-blush band-center" style="top:266px;height:69px;font-size:40px;">Drop 30 pounds</div>
    <p class="body-copy center" style="top:350px;font-size:19px;text-align:center;">With the Sunkissed Summer Slimdown.</p>
    <div class="band band-berry band-center" style="top:391px;height:41px;font-size:30px;">Comment “Summer”</div>
    <p class="line center" style="top:448px;font-size:30px;">To start now.</p>
    <p class="handle" style="top:520px;left:0;right:0;text-align:center;">@PaulaWrenLive</p>
  </section>

  <!-- Post 2 -->
  <section class="post col-right row-2" style="top:93px;">
    <p class="line blush" style="top:54px;left:33px;font-size:48px;">You can</p>
    <p class="line blush" style="top:111px;left:33px;font-size:52px;">Absolutely be down</p>
    <div class="framed-figure" style="top:189px;left:33px;width:392px;height:97px;font-size:64px;">20-30 POUNDS</div>
    <p class="line blush" style="top:311px;left:33px;font-size:34px;">By end of summer.</p>
    <p class="body-copy" style="top:361px;left:33px;font-size:15px;">It takes is the right plan—and you’ve found it.</p>
    <p class="line" style="top:394px;left:33px;font-size:50px;">Comment “Hot Girl”</p>
    <p class="body-copy" style="top:458px;left:33px;font-size:18px;">For the Sunkissed Summer Slimdown!</p>
    <p class="handle" style="top:520px;right:33px;">@PaulaWrenLive</p>
  </section>

  <!-- Post 3 -->
  <section class="post col-left row-2">
    <p class="line" style="top:79px;left:38px;font-size:44px;">You’ve got 8 weeks</p>
    <p class="line" style="top:134px;left:38px;font-size:44px;">and the perfect plan</p>
    <p class="line" style="top:189px;left:38px;font-size:44px;">to drop 30 pounds.</p>
    <p class="line blush" style="top:273px;left:38px;font-size:25px;">Let’s get snatched this summer</p>
    <p class="line blush" style="top:307px;left:38px;font-size:25px;">with the Sunkissed Summer Slimdown.</p>
    <div class="band band-berry" style="top:367px;height:70px;font-size:48px;padding-left:38px;">Comment “Summer”</div>
    <p class="handle" style="top:474px;left:38px;">@PaulaWrenLive</p>
  </section>

  <!-- Post 4 -->
  <section class="post col-right row-2">
    <p class="line center" style="top:51px;font-size:48px;">Don’t wait ‘til next</p>
    <p class="line center" style="top:109px;font-size:48px;">summer to get right</p>
    <div class="band band-blush band-center" style="top:182px;left:29px;width:402px;height:91px;font-size:62px;">The time is now</div>
    <p class="line center blush" style="top:299px;font-size:29px;">Drop 30 pounds with</p>
    <p class="line center blush" style="top:337px;font-size:29px;">the Sunkissed Summer Slimdown.</p>
    <div class="band band-berry band-center" style="top:399px;height:70px;font-size:48px;">Comment “Summer”</div>
    <p class="handle" style="top:510px;left:0;right:0;text-align:center;">@PaulaWrenLive</p>
  </section>

  <!-- Post 5 -->
  <section class="post col-left row-3">
    <p class="line" style="top:61px;left:29px;font-size:50px;">Sis, we’re dropping</p>
    <p class="line" style="top:121px;left:29px;font-size:50px;">belly flat <span class="blush">and</span></p>
    <p class="line blush" style="top:181px;left:29px;font-size:50px;">saying goodbye</p>
    <p class="line blush" style="top:241px;left:29px;font-size:50px;">to stubborn pounds</p>
    <p class="line" style="top:334px;left:29px;font-size:26px;">Join the Sunkissed Summer Slimdown</p>
    <div class="band band-berry" style="top:382px;height:70px;font-size:48px;padding-left:38px;">Comment “Summer”</div>
    <p class="handle" style="top:496px;left:29px;">@PaulaWrenLive</p>
  </section>

  <!-- Post 6 -->
  <section class="post col-right row-3">
    <p class="line" style="top:47px;left:42px;font-size:50px;">Nothing feels</p>
    <p class="line" style="top:107px;left:42px;font-size:50px;">better than <span class="blush">seeing</span></p>
    <p class="line blush" style="top:167px;left:42px;font-size:50px;">that scale drop</p>
    <p class="line blush" style="top:227px;left:42px;font-size:50px;">week after week.</p>
    <p class="line" style="top:300px;left:42px;font-size:18px;">Let’s lose up to 30 pounds this summer—together.</p>
    <div class="band band-berry" style="top:343px;height:69px;font-size:48px;padding-left:38px;">Comment “Summer”</div>
    <p class="line" style="top:441px;left:42px;font-size:23px;">To join the Sunkissed Summer Slimdown!</p>
    <p class="handle" style="top:498px;left:42px;">@PaulaWrenLive</p>
  </section>

  <!-- Post 7 -->
  <section class="post col-left row-4">
    <ul class="checklist" style="top:60px;left:37px;">
      <li><svg viewBox="0 0 46 46" aria-hidden="true"><circle cx="23" cy="23" r="23" fill="var(--berry)"/><polyline points="13,24 20,31 33,16" fill="none" stroke="#fff" stroke-width="5" stroke-linecap="round" stroke-linejoin="round"/></svg>Snatched waist</li>
      <li><svg viewBox="0 0 46 46" aria-hidden="true"><circle cx="23" cy="23" r="23" fill="var(--berry)"/><polyline points="13,24 20,31 33,16" fill="none" stroke="#fff" stroke-width="5" stroke-linecap="round" stroke-linejoin="round"/></svg>FLAT TUMMY</li>
      <li><svg viewBox="0 0 46 46" aria-hidden="true"><circle cx="23" cy="23" r="23" fill="var(--berry)"/><polyline points="13,24 20,31 33,16" fill="none" stroke="#fff" stroke-width="5" stroke-linecap="round" stroke-linejoin="round"/></svg>30 POUNDS LIGHTER</li>
    </ul>
    <p class="line blush" style="top:255px;left:37px;font-size:35px;">That’s what <span class="berry">the</span></p>
    <p class="line" style="top:298px;left:37px;font-size:35px;">Sunkissed Summer Slimdown</p>
    <p class="line" style="top:341px;left:37px;font-size:35px;">challenge <span class="blush">delivers.</span></p>
    <div class="band band-berry band-center" style="top:409px;height:57px;font-size:27px;">Comment “Hot Girl” to get the plan</div>
    <p class="handle" style="top:502px;left:37px;">@PaulaWrenLive</p>
  </section>

  <!-- Post 8 -->
  <section class="post col-right row-4">
    <p class="line blush" style="top:111px;left:31px;font-size:44px;">There’s still time</p>
    <div class="band band-berry" style="top:173px;height:50px;font-size:42px;padding-left:31px;">To drop the 30 pounds</div>
    <p class="line blush" style="top:240px;left:31px;font-size:44px;">and slay this summer.</p>
    <p class="line" style="top:311px;left:31px;font-size:18px;">The Sunkissed Summer Slimdown has the blueprint.</p>
    <p class="line" style="top:348px;left:31px;font-size:52px;">Comment “Hot Girl”!</p>
    <p class="handle" style="top:442px;left:31px;">@PaulaWrenLive</p>
  </section>

  <!-- Post 9 -->
  <section class="post col-left row-5">
    <p class="line blush" style="top:45px;left:43px;font-size:44px;">If your goal is...</p>
    <ul class="checklist" style="top:119px;left:43px;">
      <li><svg viewBox="0 0 46 46" aria-hidden="true"><circle cx="23" cy="23" r="23" fill="var(--berry)"/><polyline points="13,24 20,31 33,16" fill="none" stroke="#fff" stroke-width="5" stroke-linecap="round" stroke-linejoin="round"/></svg>TINY WAIST</li>
      <li><svg viewBox="0 0 46 46" aria-hidden="true"><circle cx="23" cy="23" r="23" fill="var(--berry)"/><polyline points="13,24 20,31 33,16" fill="none" stroke="#fff" stroke-width="5" stroke-linecap="round" stroke-linejoin="round"/></svg>FLAT BELLY</li>
      <li><svg viewBox="0 0 46 46" aria-hidden="true"><circle cx="23" cy="23" r="23" fill="var(--berry)"/><polyline points="13,24 20,31 33,16" fill="none" stroke="#fff" stroke-width="5" stroke-linecap="round" stroke-linejoin="round"/></svg>30 POUNDS DOWN</li>
    </ul>
    <p class="line blush" style="top:297px;left:43px;font-size:46px;">This is the plan.</p>
    <div class="band band-berry band-center" style="top:364px;height:70px;font-size:48px;">Comment “Summer”</div>
    <p class="line center" style="top:455px;font-size:23px;">To join the Sunkissed Summer Slimdown!</p>
    <p class="handle" style="top:520px;left:43px;">@PaulaWrenLive</p>
  </section>

  <!-- Post 10 -->
  <section class="post col-right row-5">
    <p class="line blush" style="top:60px;left:42px;font-size:42px;">This summer</p>
    <p class="line blush" style="top:112px;left:42px;font-size:42px;">ain’t over—<span class="berry">and neither</span></p>
    <p class="line" style="top:164px;left:42px;font-size:42px;">are your body goals.</p>
    <div class="band band-berry" style="top:231px;height:70px;font-size:44px;padding-left:42px;">Drop 30 pounds</div>
    <p class="line blush" style="top:322px;left:42px;font-size:21px;">With the Sunkissed Summer Slimdown.</p>
    <p class="line" style="top:370px;left:42px;font-size:44px;">Comment “Hot Girl”</p>
    <p class="line" style="top:422px;left:42px;font-size:44px;">to get the plan</p>
    <p class="handle" style="top:520px;left:42px;">@PaulaWrenLive</p>
  </section>

</main>
</body>
</html>
```